Business Card for a Mortgage Agent (myself)

I need a business card for my new job as Mortgage Agent. The Broker's logo is to be on the card as well as the brokerage License number. Not sure if to include a photo or not. Info to be on card.
Dante Roux
Mortgage Agent
Lic # M47105386
Cell: 905-614-2753
Email: danterouxk.ma@fennmail.com
Web: www.karlvostermortgages.com
TPW Brokerage Lic. # 73918

```html
<!DOCTYPE html>
<html lang="en">
<head>
<meta charset="utf-8">
<title>Dante Roux – Mortgage Agent Business Cards</title>
<link rel="stylesheet" href="https://fonts.googleapis.com/css2?family=Open+Sans:ital,wght@1,400;1,600&family=Roboto:wght@400;500&family=Rubik:wght@700&display=swap">
<style>
  :root {
    --stage: #0d4596;
    --brand-blue: #1a4fa3;
    --card-blue: #3a6cc4;
    --brand-yellow: #f5c518;
    --paper: #f7f8fa;
    --ink: #2a2f3a;
    --muted: #9aa1ad;
    --pale-blue: #a8c3ef;
    --white: #ffffff;
  }
  * { margin: 0; padding: 0; box-sizing: border-box; }
  html, body { width: 1200px; height: 706px; overflow: hidden; }
  body { background: var(--stage); font-family: "Roboto", Arial, sans-serif; position: relative; }

  .card {
    position: absolute; top: 198px;
    width: 540px; height: 309px;
    border-radius: 3px;
    box-shadow: 0 18px 40px rgba(0, 0, 0, 0.25);
    overflow: hidden;
  }
  .card--blue { left: 40px; background: var(--card-blue); }
  .card--white { left: 620px; background: var(--paper); }

  .brand-mark {
    position: absolute; left: 70px; top: 48px;
    display: flex; align-items: center; gap: 12px;
  }
  .brand-mark__square { width: 30px; height: 30px; background: var(--brand-yellow); }
  .brand-mark__name {
    font-family: "Rubik", Arial, sans-serif; font-weight: 700;
    font-size: 40px; letter-spacing: 6px;
  }
  .card--white .brand-mark__name { color: var(--brand-blue); }
  .card--blue .brand-mark__name { color: var(--white); }

  .band {
    position: absolute; top: 140px; height: 20px;
    clip-path: polygon(12px 0, 100% 0, calc(100% - 12px) 100%, 0 100%);
    font-family: "Open Sans", Arial, sans-serif; font-style: italic;
    display: flex; align-items: center;
  }
  .band--tagline { left: 38px; width: 202px; padding-left: 22px; font-size: 10px; letter-spacing: 1.2px; font-weight: 600; text-transform: uppercase; }
  .band--web { left: 246px; width: 310px; padding-left: 22px; font-size: 14px; }
  .card--white .band { background: var(--brand-blue); color: var(--white); }
  .card--blue .band { background: var(--white); color: var(--pale-blue); }

  .brokerage-licence {
    position: absolute; right: 36px; top: 168px;
    font-size: 11px;
  }
  .card--white .brokerage-licence { color: var(--muted); }
  .card--blue .brokerage-licence { color: var(--pale-blue); }

  .agent { position: absolute; left: 76px; top: 190px; }
  .agent__name { font-family: "Rubik", Arial, sans-serif; font-weight: 700; font-size: 28px; line-height: 1.1; }
  .agent__title {
    font-size: 18px; padding-bottom: 4px; padding-right: 14px;
    border-bottom: 2px solid var(--brand-yellow); display: inline-block;
  }
  .agent__licence { font-size: 11px; margin-top: 6px; }
  .card--white .agent__name { color: var(--brand-blue); }
  .card--white .agent__title { color: var(--ink); }
  .card--white .agent__licence { color: var(--muted); }
  .card--blue .agent__name { color: var(--brand-yellow); }
  .card--blue .agent__title { color: var(--white); }
  .card--blue .agent__licence { color: var(--pale-blue); }

  .contact { position: absolute; left: 300px; top: 228px; font-size: 16px; line-height: 1.45; }
  .card--white .contact { color: #6b7280; }
  .card--blue .contact { color: #e3ebf8; }
</style>
</head>
<body>
  <section class="card card--blue" aria-label="Business card, blue side">
    <div class="brand-mark"><span class="brand-mark__square"></span><span class="brand-mark__name">TPW</span></div>
    <div class="band band--tagline">True Pine Wealth</div>
    <div class="band band--web">www.karlvostermortgages.com</div>
    <p class="brokerage-licence">TPW Brokerage Lic. # 73918</p>
    <div class="agent">
      <h1 class="agent__name">Dante Roux</h1>
      <p class="agent__title">Mortgage Agent</p>
      <p class="agent__licence">Lic # M47105386</p>
    </div>
    <div class="contact">
      <p>phone: 905-614-2753</p>
      <p>danterouxk.ma@fennmail.com</p>
    </div>
  </section>

  <section class="card card--white" aria-label="Business card, white side">
    <div class="brand-mark"><span class="brand-mark__square"></span><span class="brand-mark__name">TPW</span></div>
    <div class="band band--tagline">True Pine Wealth</div>
    <div class="band band--web">www.karlvostermortgages.com</div>
    <p class="brokerage-licence">TPW Brokerage Lic. # 73918</p>
    <div class="agent">
      <h2 class="agent__name">Dante Roux</h2>
      <p class="agent__title">Mortgage Agent</p>
      <p class="agent__licence">Lic # M47105386</p>
    </div>
    <div class="contact">
      <p>phone: 905-614-2753</p>
      <p>danterouxk.ma@fennmail.com</p>
    </div>
  </section>
</body>
</html>
```